IT business looking for Standout Letterhead Design

We need a letterhead design for a company based in Marlow Bay, CA called Corvane Systems, Inc. We specialize in IT engineering, installation and technical support pertaining to the department of defense.

We would like to see a design that incorporates the black and gold that matches our company logo.

More information on the company can be found at www.corvane-sys.example

```html
<!DOCTYPE html>
<html lang="en">
<head>
<meta charset="utf-8">
<title>Corvane Systems, Inc. — Letterhead</title>
<link href="https://fonts.googleapis.com/css2?family=Cinzel:wght@600&family=Open+Sans:wght@400&display=swap" rel="stylesheet">
<style>
  :root {
    --backdrop: #e9e6e1;
    --paper: #ffffff;
    --ink: #1f1f1f;
    --ink-soft: #4a4a4a;
    --rule: #b9b9b9;
    --band-black: #232323;
    --gold-light: #f3e21c;
    --gold-mid: #e2b21b;
    --gold-deep: #a86a1c;
    --watermark: #ededed;
  }
  * { box-sizing: border-box; margin: 0; padding: 0; }
  html, body { width: 1186px; height: 1200px; overflow: hidden; }
  body { background: var(--backdrop); font-family: "Open Sans", Arial, sans-serif; color: var(--ink); }

  .letterhead {
    position: absolute; left: 168px; top: 50px;
    width: 850px; height: 1100px;
    background: var(--paper);
    box-shadow: 0 4px 18px rgba(0,0,0,.18);
    overflow: hidden;
  }

  .brand { position: absolute; left: 52px; top: 48px; display: flex; align-items: center; gap: 12px; }
  .brand-dot { width: 18px; height: 18px; border-radius: 50%; background: var(--gold-mid); }
  .brand-name { font-family: "Cinzel", Georgia, serif; font-weight: 600; font-size: 26px; color: var(--ink); letter-spacing: .5px; }

  .contact {
    position: absolute; right: 48px; top: 170px;
    border-left: 1px solid var(--rule); padding-left: 10px;
    font-style: normal;
    font-size: 12.5px; line-height: 20px; color: var(--ink-soft);
  }
  .contact-item { display: flex; align-items: center; gap: 7px; }
  .contact-item svg { width: 11px; height: 11px; fill: var(--ink-soft); flex: none; }

  .watermark {
    position: absolute; left: 0; right: 0; top: 470px; text-align: center;
    font-family: "Cinzel", Georgia, serif; font-weight: 600; font-size: 58px;
    color: var(--watermark); letter-spacing: 2px;
  }

  .location {
    position: absolute; right: 50px; bottom: 40px;
    display: flex; align-items: center; gap: 7px;
    font-size: 19px; color: var(--ink-soft);
  }
  .location svg { width: 15px; height: 15px; fill: var(--ink-soft); }

  .footer-bands { position: absolute; left: 0; bottom: 0; width: 850px; height: 24px; display: block; }
</style>
</head>
<body>
  <main class="letterhead">
    <header class="brand">
      <span class="brand-dot"></span>
      <span class="brand-name">Corvane Systems, Inc.</span>
    </header>

    <address class="contact">
      <div class="contact-item">
        <svg viewBox="0 0 24 24"><path d="M6.6 10.8a15 15 0 0 0 6.6 6.6l2.2-2.2a1 1 0 0 1 1-.25 11.4 11.4 0 0 0 3.6.57 1 1 0 0 1 1 1V20a1 1 0 0 1-1 1A17 17 0 0 1 3 4a1 1 0 0 1 1-1h3.5a1 1 0 0 1 1 1c0 1.25.2 2.45.57 3.6a1 1 0 0 1-.25 1z"/></svg>
        <span>555-014-2273</span>
      </div>
      <div class="contact-item">
        <svg viewBox="0 0 24 24"><path d="M6 3h12v5H6zM4 9h16a2 2 0 0 1 2 2v6h-4v4H6v-4H2v-6a2 2 0 0 1 2-2zm4 7v3h8v-3z"/></svg>
        <span>555-014-2290</span>
      </div>
      <div class="contact-item">
        <svg viewBox="0 0 24 24"><path d="M2 5h20v14H2zm2 2v.5l8 5 8-5V7l-8 5z"/></svg>
        <span>info@corvane-sys.example</span>
      </div>
      <div class="contact-item">
        <svg viewBox="0 0 24 24"><path d="M12 2a10 10 0 1 0 0 20 10 10 0 0 0 0-20zm0 2c.9 1.2 1.6 2.7 2 4h-4c.4-1.3 1.1-2.8 2-4zM4.3 14a8 8 0 0 1 0-4h3.4a16 16 0 0 0 0 4zm.9 2h3c.3 1.2.8 2.4 1.4 3.4A8 8 0 0 1 5.2 16zm3-8h-3a8 8 0 0 1 4.4-3.4C8 5.6 7.6 6.8 8.2 8zM12 20c-.9-1.2-1.6-2.7-2-4h4c-.4 1.3-1.1 2.8-2 4zm2.3-6H9.7a14 14 0 0 1 0-4h4.6a14 14 0 0 1 0 4zm.1 5.4c.6-1 1.1-2.2 1.4-3.4h3a8 8 0 0 1-4.4 3.4zM16.3 14a16 16 0 0 0 0-4h3.4a8 8 0 0 1 0 4z"/></svg>
        <span>www.corvane-sys.example</span>
      </div>
    </address>

    <div class="watermark" aria-hidden="true">Corvane Systems, Inc.</div>

    <div class="location">
      <svg viewBox="0 0 24 24"><path d="M12 2a7 7 0 0 0-7 7c0 5 7 13 7 13s7-8 7-13a7 7 0 0 0-7-7zm0 9.5A2.5 2.5 0 1 1 12 6.5a2.5 2.5 0 0 1 0 5z"/></svg>
      <span>Marlow Bay, CA</span>
    </div>

    <svg class="footer-bands" viewBox="0 0 850 24" preserveAspectRatio="none" aria-hidden="true">
      <defs>
        <linearGradient id="goldBand" x1="0" y1="0" x2="1" y2="0">
          <stop offset="0" stop-color="var(--gold-light)"/>
          <stop offset=".45" stop-color="var(--gold-mid)"/>
          <stop offset="1" stop-color="var(--gold-deep)"/>
        </linearGradient>
      </defs>
      <polygon points="0,0 372,0 356,12 0,12" fill="var(--band-black)"/>
      <polygon points="376,4 850,4 850,24 350,24" fill="url(#goldBand)"/>
    </svg>
  </main>
</body>
</html>
```